In Home Personal IT Consultant (Nerd) Website and Logo QTgeek.net

Website and logo design for in home personal "nerd". Consulting services provided: Home Automation, Home Theater, Network and Wi-Fi installation, Computer Repair, and Virus Removal. Need simple site to promote QTgeek.net based in Santa Fe, New Mexico. You may choose to incorporate the Zia symbol from the New Mexico flag into the design, not mandatory. I am also a big fan of the movie Return of the Tinkers.
I have over 10 years of experience in the hospitality industry working with multi million dollar hotels and will apply that same level of service to the home. TechVara B+ and Shieldwise+ Certified. Available by appointment, primarily Evenings and Weekends. Consulting rate will be $70/hr.
Industry/Entity Type
Consulting
Number of Pages Required
1 page
Look and feel
Each slider illustrates characteristics of the customer's brand and the style your logo design should communicate.

```html
<!DOCTYPE html>
<html lang="en">
<head>
<meta charset="utf-8">
<title>Pricing</title>
<link rel="stylesheet" href="https://fonts.googleapis.com/css2?family=PT+Sans:wght@400;700&display=swap">
<style>
:root{
  --ink:#082a33;
  --text:#0d1e24;
  --accent:#e0195a;
  --muted:#b5c0c4;
  --muted-text:#a3adb1;
  --rule:#a7a7a9;
  --paper:#ffffff;
}
*{margin:0;padding:0;box-sizing:border-box}
html,body{width:1200px;height:700px;overflow:hidden;background:var(--paper)}
body{position:relative;font-family:"PT Sans",Arial,sans-serif;color:var(--text)}

.section-title{position:absolute;top:42px;left:0;width:1200px;text-align:center;font-size:29px;font-weight:700;color:var(--ink)}
.title-rule{position:absolute;top:93px;left:487px;width:226px;height:6px;border-radius:3px;background:var(--rule)}

.intro{position:absolute;left:110px;width:980px;text-align:center;font-size:17.5px;line-height:24px}
.intro--first{top:148px}
.intro--second{top:253px}

.calendar{position:absolute;left:143px;top:350px;width:556px;height:300px;background:var(--ink)}
.calendar-head{position:absolute;top:370px;left:143px;width:556px;height:40px;display:flex;justify-content:center;gap:28px;font-size:27px;font-weight:700;color:var(--paper)}
.calendar-head span{text-shadow:2px 2px 0 #6c7b80}
.calendar-head b{color:var(--accent);font-weight:400;text-shadow:none}
.calendar-head .day{font-size:31px;margin-top:-3px}
.calendar-body{position:absolute;left:150px;top:428px;width:541px;height:213px;background:var(--paper)}

.days{position:absolute;left:174px;top:452px;display:grid;grid-template-columns:repeat(7,45px);column-gap:4.5px;row-gap:12px;font-size:17px;text-align:center}
.days span{height:18px;line-height:18px}
.days .weekday{background:var(--ink);color:var(--paper);font-size:17px;margin-bottom:6px}
.days .weekend{background:var(--muted)}
.days .busy{background:var(--muted)}
.days .other{color:var(--muted-text)}

.months{position:absolute;left:521px;top:452px;display:grid;grid-template-columns:repeat(3,43px);column-gap:6px;row-gap:6px}
.months span{height:37px;background:var(--ink);color:var(--paper);font-size:18px;display:flex;align-items:center;justify-content:center}
.months .current{background:var(--accent)}

.appointment{position:absolute;left:778px;top:350px;width:280px;height:300px;background:var(--ink)}
.appointment-title{position:absolute;left:778px;top:363px;width:280px;text-align:center;color:var(--paper);font-size:18.5px;font-weight:700;line-height:24px}
.appointment-card{position:absolute;left:786px;top:428px;width:265px;height:168px;background:var(--paper)}
.appointment-note{position:absolute;left:810px;top:449px;width:220px;font-size:9.3px;line-height:12px}
.rate-rule{position:absolute;left:810px;width:216px;height:4px;border-radius:2px;background:var(--rule)}
.rate-rule--top{top:506px}
.rate-rule--bottom{top:540px}
.rate-label{position:absolute;left:786px;top:513px;width:265px;text-align:center;font-size:17px;font-weight:700}
.rate-value{position:absolute;left:786px;top:544px;width:265px;text-align:center;font-size:37px;font-weight:700;color:var(--accent)}
.appointment-request{position:absolute;left:786px;top:604px;width:265px;height:38px;background:var(--paper);text-align:center;line-height:38px;font-size:18px;font-weight:700}

.footer-band{position:absolute;left:122px;top:690px;width:956px;height:20px;border-radius:10px;background:var(--ink)}
</style>
</head>
<body>
<h1 class="section-title">Pricing</h1>
<div class="title-rule"></div>

<p class="intro intro--first">Lorem ipsum dolor sit amet, consectetuer adipiscing elit. Aenean commodo ligula eget dolor. Aenean massa. Cum sociis natoque penatibus etnes magnis dis parturient montes, nascetur ridiculus mus. Nullam quis ante. Etiam sito metorci eget eros faucibus tincidunt. Duis pasi leo. Sed fringilla mauris sit amet nibh. Donec sodales sagittis magna.</p>
<p class="intro intro--second">Nullam quis ante. Etiam sit amet orcide eget eros faucibus tincidunt. Duis leo. Sed fringilla ifus mauris sit amet nibh. Donec sodales sagittis magna. Donec sodales sagittis magna. Sed consequat, leo eget bibendum sodales.</p>

<div class="calendar"></div>
<div class="calendar-head">
  <div><b>[</b><span>November</span><b>]</b></div>
  <div><b>[</b><span class="day">11</span><b>]</b></div>
  <div><b>[</b><span>2017</span><b>]</b></div>
</div>
<div class="calendar-body"></div>

<div class="days">
  <span class="weekday">mo</span><span class="weekday">tu</span><span class="weekday">we</span><span class="weekday">th</span><span class="weekday">fr</span><span class="weekday weekend">sa</span><span class="weekday weekend">su</span>
  <span class="other">30</span><span class="other">31</span><span>1</span><span>2</span><span>3</span><span>4</span><span class="busy">5</span>
  <span>6</span><span>7</span><span>8</span><span class="busy">9</span><span>10</span><span class="busy">11</span><span>12</span>
  <span class="busy">13</span><span>14</span><span class="busy">15</span><span>16</span><span>17</span><span class="busy">18</span><span class="busy">19</span>
  <span>20</span><span>21</span><span>22</span><span>23</span><span>24</span><span>25</span><span class="busy">26</span>
  <span>27</span><span>28</span><span>29</span><span>30</span><span class="other">1</span><span class="other">2</span><span class="other">3</span>
</div>

<div class="months">
  <span>jan</span><span>feb</span><span>mar</span>
  <span>apr</span><span>may</span><span>jun</span>
  <span>jul</span><span>aug</span><span>sep</span>
  <span>oct</span><span class="current">nov</span><span>dec</span>
</div>

<div class="appointment"></div>
<h2 class="appointment-title">Make an<br>appointment</h2>
<div class="appointment-card"></div>
<p class="appointment-note">Lorem ipsum dolor sit amet, consectetuer adipi scing elit. Aenean commodo ligula eget dolor. Aenean massa. Etiam sit amet orci eget eros faucon ibus tincidunt. Sed fringilla mauris sit amet nibh.</p>
<div class="rate-rule rate-rule--top"></div>
<div class="rate-label">payment rate</div>
<div class="rate-rule rate-rule--bottom"></div>
<div class="rate-value">$ 70/hr</div>
<div class="appointment-request">Request an appointment</div>

<div class="footer-band"></div>
</body>
</html>
```